Bellwood Tax
Project: Business Cards and Stationery
Business Cards and Stationery - Consulting
Business Cards and Stationery
Modern
Peter Marsh
President
28617 Coralind Ave., 4th Floor Sherman Oaks, CA 90572
peterm@bellwdtax.example
www.bellwoodtaxservice.example

```html
<!DOCTYPE html>
<html lang="en">
<head>
<meta charset="utf-8">
<title>Bellwood Tax – Business Card</title>
<link href="https://fonts.googleapis.com/css2?family=Cinzel:wght@400;600&display=swap" rel="stylesheet">
<style>
  :root {
    --page-bg: #e9e7e4;
    --card-white: #ffffff;
    --brand-blue: #3db4e8;
    --brand-dark: #2f2f31;
    --text-dark: #3a3a3c;
    --text-light: #ffffff;
  }
  * { margin: 0; padding: 0; box-sizing: border-box; }
  html, body {
    width: 1200px; height: 900px; overflow: hidden;
    background: var(--page-bg);
    font-family: "Cinzel", "Trajan Pro", serif;
  }
  .card {
    position: absolute; left: 75px; top: 150px;
    width: 1050px; height: 600px;
    background: var(--card-white);
    box-shadow: 0 10px 30px rgba(0,0,0,0.18);
    overflow: hidden;
  }
  .card__band {
    position: absolute; left: 0; right: 0; top: 272px; bottom: 0;
    background: var(--brand-blue);
  }
  .brand {
    position: absolute; left: 68px; top: 108px;
    display: flex; align-items: center; gap: 24px;
  }
  .brand__dot {
    width: 86px; height: 86px; border-radius: 50%;
    background: var(--brand-blue);
  }
  .brand__name {
    font-size: 60px; font-weight: 400; letter-spacing: 1px;
    color: var(--text-dark); line-height: 1;
  }
  .name-tab {
    position: absolute; right: 0; top: 220px;
    width: 420px; height: 118px;
    background: var(--brand-dark);
    clip-path: polygon(0 0, 100% 0, 100% 100%, 40px 100%, 0 62%);
    color: var(--text-light); text-align: center;
    padding: 22px 0 0 30px;
  }
  .name-tab__name { font-size: 30px; letter-spacing: 1px; }
  .name-tab__title { font-size: 21px; letter-spacing: 2px; margin-top: 4px; }
  .contact {
    position: absolute; left: 52px; top: 392px;
    list-style: none; color: var(--text-light);
    font-size: 19px; letter-spacing: 0.5px;
  }
  .contact__item { display: flex; align-items: flex-start; gap: 12px; line-height: 28px; }
  .contact__icon { width: 22px; height: 22px; margin-top: 3px; flex: none; }
  .website {
    position: absolute; right: 56px; top: 425px;
    color: var(--text-light); font-size: 24px; letter-spacing: 2px;
  }
</style>
</head>
<body>
  <div class="card">
    <div class="card__band"></div>

    <div class="brand">
      <div class="brand__dot"></div>
      <div class="brand__name">BELLWOOD TAX</div>
    </div>

    <div class="name-tab">
      <div class="name-tab__name">PETER MARSH</div>
      <div class="name-tab__title">PRESIDENT</div>
    </div>

    <ul class="contact">
      <li class="contact__item">
        <svg class="contact__icon" viewBox="0 0 22 22"><circle cx="11" cy="11" r="11" fill="#fff"/><path d="M5 11 L11 5.5 L17 11 H15 V16 H7 V11 Z" fill="#3db4e8"/></svg>
        <span>28617 Coralind Ave., 4th Floor<br>Sherman Oaks, CA 90572</span>
      </li>
      <li class="contact__item">
        <svg class="contact__icon" viewBox="0 0 22 22"><circle cx="11" cy="11" r="11" fill="#fff"/><path d="M7.5 5.5 L9.5 5.5 L10.5 8.5 L9 9.8 Q10.3 12.2 12.2 13 L13.5 11.5 L16.5 12.5 L16.5 14.5 Q15 16.5 12 15.5 Q7 13 6 8.5 Q6 6.5 7.5 5.5 Z" fill="#3db4e8"/></svg>
        <span>800-555-0142</span>
      </li>
      <li class="contact__item">
        <svg class="contact__icon" viewBox="0 0 22 22"><circle cx="11" cy="11" r="11" fill="#fff"/><rect x="6" y="9" width="10" height="6" fill="#3db4e8"/><rect x="8" y="5.5" width="6" height="3" fill="#3db4e8"/></svg>
        <span>800-555-0148</span>
      </li>
      <li class="contact__item">
        <svg class="contact__icon" viewBox="0 0 22 22"><circle cx="11" cy="11" r="11" fill="#fff"/><rect x="5.5" y="7" width="11" height="8" fill="#3db4e8"/><path d="M5.5 7 L11 11.5 L16.5 7" stroke="#fff" stroke-width="1.2" fill="none"/></svg>
        <span>PETERM@BELLWDTAX.EXAMPLE</span>
      </li>
    </ul>

    <div class="website">www.bellwoodtaxservice.example</div>
  </div>
</body>
</html>
```